依頼詳細
依頼の詳細や参考URL等は添付の「依頼詳細.txt」に全てまとめましたので、そちらをご確認ください。
トップページのラフイメージは「toppage_image.jpg」を参照下さい。
サイトURL
ページ数
1ページ
希望イメージ
シンプル 複雑
単色 カラフル
暗い 明るい
日常 高級
遊び心 厳粛
未来的 伝統的
女性的 男性的
希望する色
背景色:アイボリー。差し色:薄紫色など淡い色で何色か使用。
納品ファイル
• イラストレーター形式 (.ai)
• フォトショップ形式 (.psd)
補足説明

レベルがみなさん高かったので非常に迷いましたが、水彩がうまくマッチしていて、ごあいさつや保育目標などの部分のデザインも気に入りましたのでこちらにしました。

今回はコンペに参加していただき、誠にありがとうございました。
みなさん素晴らしいデザインで迷いましたが、またコンペを依頼する際にはご提案していただけたら幸いです。

```html
<!DOCTYPE html>
<html lang="ja">
<head>
<meta charset="utf-8">
<title>ひなた保育園</title>
<link href="https://fonts.googleapis.com/css2?family=Zen+Maru+Gothic:wght@400;500;700&display=swap" rel="stylesheet">
<style>
:root{
  --ivory:#f8f5ec;
  --ink:#6b5a4a;
  --ink-soft:#8c7c6b;
  --pink:#f2b8bc;
  --pink-deep:#e7929a;
  --yellow:#f6dc86;
  --blue:#b9d9ea;
  --lilac:#cdbde3;
  --lilac-deep:#b7a3d6;
  --green:#a9cf9a;
  --beige:#efe3c4;
  --nav-line:#d9cfbd;
}
*{margin:0;padding:0;box-sizing:border-box}
html,body{width:1200px;height:4004px;overflow:hidden}
body{background:var(--ivory);font-family:"Zen Maru Gothic",sans-serif;color:var(--ink);position:relative}
.abs{position:absolute}
.ph{position:absolute;display:block}

/* header */
.header-art{left:0;top:0;width:1200px;height:240px;background:linear-gradient(180deg,#f6d3d4 0%,#f8e6cf 60%,var(--ivory) 100%)}
.org-line{left:24px;top:12px;font-size:13px;color:var(--ink-soft)}
.logo{left:0;width:1200px;top:100px;text-align:center}
.logo-name{font-size:50px;font-weight:700;letter-spacing:.18em;color:var(--ink)}
.logo-sub{font-size:15px;letter-spacing:.2em;color:var(--ink-soft);margin-top:4px}
.logo-dot{display:inline-block;width:14px;height:14px;border-radius:50%;background:var(--yellow);margin-right:12px;vertical-align:middle}
.nav{left:150px;top:296px;width:900px;height:48px;display:flex;border-top:1px solid var(--nav-line);border-bottom:1px solid var(--nav-line)}
.nav a{flex:1;text-align:center;line-height:46px;font-size:16px;color:var(--ink);text-decoration:none;border-left:1px dashed var(--nav-line)}
.nav a:first-child{border-left:none}
.nav a.current{color:var(--pink-deep)}

/* hero */
.hero-side{top:392px;height:320px;width:220px;opacity:.45}
.hero-main{left:220px;top:385px;width:760px;height:330px;border:6px solid #fff;background:linear-gradient(135deg,#7fa0b7,#b8c79a 55%,#d49b9b)}
.hero-caption{left:0;width:1200px;top:738px;text-align:center;font-size:14px;color:var(--ink-soft)}

/* section headings */
.heading{left:460px;width:280px;height:60px;border-radius:30px;display:flex;align-items:center;justify-content:center;font-size:26px;font-weight:700;color:#fff;letter-spacing:.12em}

/* greeting */
.greeting-text{left:0;width:1200px;top:900px;text-align:center;font-size:18px;line-height:2.45;color:var(--ink)}
.birds-left{left:230px;top:900px;width:110px;height:90px;border-radius:40px;background:linear-gradient(135deg,var(--pink),var(--pink-deep));opacity:.7}
.bird-right{left:820px;top:1220px;width:60px;height:44px;border-radius:50%;background:var(--green);opacity:.7}

/* features */
.feature-band{left:0;top:1470px;width:1200px;height:330px;background:linear-gradient(90deg,#8a7f74,#e3a4ae 35%,#b8c6d9 65%,#c75a5a)}
.feature-text{left:0;width:1200px;top:1840px;text-align:center;font-size:17px;line-height:2.3}
.feature-mark{left:200px;top:1838px;width:96px;height:70px;border-radius:50%;background:var(--blue);opacity:.8}
.grid{left:225px;top:2060px;width:750px;display:grid;grid-template-columns:repeat(3,230px);column-gap:30px;row-gap:34px}
.card-tag{display:inline-block;background:var(--green);color:#fff;font-size:13px;padding:3px 16px;margin-bottom:10px}
.card-photo{position:relative;height:150px}
.card-text{font-size:13px;line-height:1.7;margin-top:10px;color:var(--ink)}

.divider{left:0;top:2800px;width:1200px;border-top:2px dashed var(--nav-line)}

/* goals */
.goal-band{left:0;top:2990px;width:1200px;height:310px;background:linear-gradient(90deg,#d9c8b6,#f0ece4 40%,#b9c7d4 70%,#b6c48f)}
.goal{top:3340px;width:170px;height:150px;border-radius:50%;display:flex;align-items:center;justify-content:center;text-align:center;font-size:14px;line-height:1.7;padding:18px}
.birds-row{top:3540px;height:60px;width:120px;border-radius:30px;opacity:.75}

/* footer */
.footer-art{left:0;top:3620px;width:1200px;height:384px;background:linear-gradient(180deg,var(--ivory) 0%,var(--beige) 22%,var(--beige) 100%)}
.footer-nav{top:3790px;font-size:13px;line-height:2.1;list-style:none}
.footer-nav li::before{content:"";display:inline-block;width:8px;height:8px;border-radius:50%;background:var(--pink);margin-right:8px}
.footer-address{left:0;width:1200px;top:3900px;text-align:center;font-size:13px;line-height:1.8;color:var(--ink)}
.footer-btn{left:880px;top:3870px;width:110px;height:28px;border-radius:4px;background:var(--pink);color:#fff;font-size:12px;text-align:center;line-height:28px}
.plants{height:110px;width:150px;border-radius:60px 60px 0 0;opacity:.65}
</style>
</head>
<body>

<header>
  <div class="ph header-art" role="img" aria-label="水彩の雲と小鳥のイラスト"></div>
  <p class="abs org-line">（社福）ひなた福祉会　ひなた保育園　みどり市こもれび町</p>
  <div class="abs logo">
    <div class="logo-name"><span class="logo-dot"></span>ひなた保育園</div>
    <div class="logo-sub">きょうも げんきに</div>
  </div>
  <nav class="abs nav">
    <a class="current">トップページ</a><a>園の案内</a><a>保育の特色</a><a>保育園の一日</a><a>年間行事</a><a>おしらせ</a><a>園児募集</a>
  </nav>
</header>

<main>
  <div class="ph hero-side" style="left:0;background:linear-gradient(135deg,#c9b48f,#e3c9c9)" role="img" aria-label="園庭で遊ぶ子どもたちの写真"></div>
  <div class="ph hero-side" style="left:980px;background:linear-gradient(135deg,#b8c9d9,#d9c7a8)" role="img" aria-label="園舎と子どもたちの写真"></div>
  <div class="ph hero-main" role="img" aria-label="帽子をかぶって遊具で遊ぶ子どもたちの写真"></div>
  <p class="abs hero-caption">みんなで、なかよくあそんだよ。</p>

  <h2 class="abs heading" style="top:803px;background:var(--pink-deep)">ごあいさつ</h2>
  <div class="ph birds-left" role="img" aria-label="飛んでいる小鳥のイラスト"></div>
  <p class="abs greeting-text">
    「豊かな自然とふれあい、健康な心身を育む」を大切に<br>
    毎日を保育の中で過ごします。<br>
    子どもひとりひとりの個性を尊重し見守ります。<br>
    保護者の皆さまと手を取り合い、地域とともに歩む保育園を目指します。<br>
    「家庭的」な雰囲気と、落ち着いた環境の中で<br>
    楽しく遊び学ぶ毎日を届けていきます。<br>
    また、日々の保育の様子をおしらせしていきます。<br>
    今後とも変わらぬご支援をお願い申し上げます。
  </p>
  <div class="ph bird-right" role="img" aria-label="小鳥のイラスト"></div>

  <h2 class="abs heading" style="top:1381px;background:var(--yellow)">園の特色</h2>
  <div class="ph feature-band" role="img" aria-label="空を指さす子どもたちの写真"></div>
  <div class="ph feature-mark" role="img" aria-label="小さな動物のイラスト"></div>
  <p class="abs feature-text">
    当園では毎日の生活を大切にしています。<br>
    カリキュラムの枠にとらわれず、自然体験を取り入れた保育を展開しています。<br>
    異年齢の子どもが関わり合い、思いやりの心を育てる一日一日を<br>
    のびのびと過ごせるよう保育士全員で見守っています。
  </p>

  <div class="abs grid">
    <div><span class="card-tag">食育</span><div class="ph card-photo" style="background:linear-gradient(135deg,#d3b48b,#8fa7b6)" role="img" aria-label="給食の様子の写真"></div><p class="card-text">旬の食材を使った給食で食べる楽しさを伝えています。</p></div>
    <div><span class="card-tag">英語</span><div class="ph card-photo" style="background:linear-gradient(135deg,#c9c6bd,#8d8b84)" role="img" aria-label="教室の黒板の写真"></div><p class="card-text">歌やゲームを通して楽しく英語にふれています。</p></div>
    <div><span class="card-tag">体操</span><div class="ph card-photo" style="background:linear-gradient(135deg,#a65a52,#d9b38c)" role="img" aria-label="体を動かす子どもたちの写真"></div><p class="card-text">専門の先生と一緒に体を動かす時間を設けています。</p></div>
    <div><span class="card-tag">音楽</span><div class="ph card-photo" style="background:linear-gradient(135deg,#f1ead8,#c8904f)" role="img" aria-label="カスタネットの写真"></div><p class="card-text">リズム遊びや合奏で音楽に親しんでいます。</p></div>
    <div><span class="card-tag">行事</span><div class="ph card-photo" style="background:linear-gradient(135deg,#c98a62,#6f8f6a)" role="img" aria-label="行事に参加する子どもたちの写真"></div><p class="card-text">季節ごとの行事で地域の方とも交流しています。</p></div>
    <div><span class="card-tag">自然</span><div class="ph card-photo" style="background:linear-gradient(135deg,#7e9a6a,#b59a7a)" role="img" aria-label="畑で作業する子どもたちの写真"></div><p class="card-text">畑で野菜を育て収穫する喜びを体験しています。</p></div>
  </div>

  <div class="abs divider"></div>

  <h2 class="abs heading" style="top:2901px;background:var(--lilac-deep)">保育目標</h2>
  <div class="ph goal-band" role="img" aria-label="園舎の前で手を広げる子どもたちの写真"></div>

  <div class="abs goal" style="left:225px;background:var(--pink)">心も体も元気で<br>明るい子ども</div>
  <div class="abs goal" style="left:420px;background:var(--blue)">思いやりのある<br>やさしい子ども</div>
  <div class="abs goal" style="left:615px;background:var(--yellow)">自分で考えて<br>行動できる子ども</div>
  <div class="abs goal" style="left:810px;background:var(--lilac)">感じたことを<br>表現できる子ども</div>

  <div class="ph birds-row" style="left:330px;background:linear-gradient(90deg,#f0c27a,#e79a5a)" role="img" aria-label="飛んでいる小鳥のイラスト"></div>
  <div class="ph birds-row" style="left:760px;background:linear-gradient(90deg,#a8cde2,#7fb1d1)" role="img" aria-label="飛んでいる小鳥のイラスト"></div>
</main>

<footer>
  <div class="ph footer-art" role="img" aria-label="水彩の雲の縁取りのイラスト"></div>
  <div class="ph plants" style="left:40px;top:3894px;background:linear-gradient(180deg,var(--green),#d9c98f)" role="img" aria-label="草花のイラスト"></div>
  <div class="ph plants" style="left:1010px;top:3894px;background:linear-gradient(180deg,var(--green),var(--pink))" role="img" aria-label="草花と小鳥のイラスト"></div>
  <ul class="abs footer-nav" style="left:340px"><li>トップページ</li><li>保育の特色</li></ul>
  <ul class="abs footer-nav" style="left:540px"><li>園の案内</li><li>保育園の一日</li></ul>
  <ul class="abs footer-nav" style="left:700px"><li>年間行事</li><li>おしらせ</li></ul>
  <ul class="abs footer-nav" style="left:840px"><li>園児募集</li><li>お問い合わせ</li></ul>
  <p class="abs footer-address">（社福）ひなた福祉会　ひなた保育園<br>〒000-0000　みどり市こもれび町1-2-3<br>TEL 000-000-0000　FAX 000-000-0001</p>
  <div class="abs footer-btn">お問い合わせ</div>
</footer>

</body>
</html>
```